BRL business card

For a business card with our logo

Contact Information for Business Card

Mathéo VRANEL
Founder & CEO
email : ceo@brightlanterncollective.com / www.brightlanterncollective.com /
instagram / facebook / WhatsApp
N°: +590 690 482 517

Colors

Designer to choose colors to be used in the design.

```html
<!DOCTYPE html>
<html lang="en">
<head>
<meta charset="utf-8">
<title>BRL Business Card</title>
<link href="https://fonts.googleapis.com/css2?family=Playfair+Display:wght@400;700&display=swap" rel="stylesheet">
<style>
  :root {
    --backdrop: #1b70ad;
    --card: #373737;
    --card-edge: #e8792f;
    --orange: #f08434;
    --blue: #2a6fc4;
    --ink-light: #f2f2f2;
    --muted: #d9d9d9;
  }
  * { box-sizing: border-box; margin: 0; padding: 0; }
  html, body {
    width: 1200px; height: 857px; overflow: hidden;
    background: var(--backdrop);
    font-family: "Playfair Display", Georgia, serif;
  }
  .canvas {
    position: relative; width: 1200px; height: 857px;
    display: flex; align-items: center; justify-content: center; gap: 60px;
  }
  .card {
    position: relative; width: 510px; height: 292px;
    background: var(--card);
    border: 3px solid var(--card-edge);
    box-shadow: 0 18px 40px rgba(0, 0, 0, 0.3);
  }

  /* Front */
  .card--front {
    display: flex; flex-direction: column; align-items: center; justify-content: center; gap: 16px;
  }
  .brand-dot {
    width: 76px; height: 76px; border-radius: 50%; background: var(--orange);
  }
  .brand-name {
    display: flex; align-items: center; gap: 12px;
    color: var(--blue); font-weight: 400; font-size: 22px; letter-spacing: 2px; text-transform: uppercase;
  }
  .brand-name::before, .brand-name::after {
    content: ""; width: 26px; height: 1px; background: var(--orange);
  }

  /* Back */
  .card--back { display: flex; align-items: center; padding: 0 30px; }
  .back-brand {
    width: 190px; display: flex; flex-direction: column; align-items: center; gap: 12px;
  }
  .back-brand .brand-dot { width: 56px; height: 56px; }
  .back-brand .brand-name { font-size: 13px; letter-spacing: 1px; gap: 6px; text-align: center; }
  .back-brand .brand-name::before, .back-brand .brand-name::after { width: 12px; }

  .contact {
    margin-left: 30px; padding-left: 18px; border-left: 1px solid var(--orange);
  }
  .contact-name { font-weight: 700; font-size: 19px; letter-spacing: 1.5px; text-transform: uppercase; }
  .contact-name .first { color: var(--orange); }
  .contact-name .last { color: var(--blue); }
  .contact-role { color: var(--muted); font-size: 10px; letter-spacing: 2px; margin: 2px 0 12px; }
  .contact-list { list-style: none; display: flex; flex-direction: column; gap: 7px; }
  .contact-list li {
    display: flex; align-items: center; gap: 8px;
    color: var(--ink-light); font-size: 10.5px; font-weight: 700;
  }
  .contact-list svg { width: 13px; height: 13px; flex: none; }
  .socials { display: flex; gap: 14px; margin-top: 12px; }
  .social-slot {
    width: 14px; height: 14px; border: 1.2px solid var(--orange); border-radius: 3px;
  }
</style>
</head>
<body>
<main class="canvas">
  <section class="card card--front" aria-label="Card front">
    <div class="brand-dot"></div>
    <div class="brand-name">Bright Lantern Collective</div>
  </section>

  <section class="card card--back" aria-label="Card back">
    <div class="back-brand">
      <div class="brand-dot"></div>
      <div class="brand-name">Bright Lantern Collective</div>
    </div>
    <div class="contact">
      <h1 class="contact-name"><span class="first">Mathéo</span> <span class="last">Vranel</span></h1>
      <p class="contact-role">Founder &amp; CEO</p>
      <ul class="contact-list">
        <li>
          <svg viewBox="0 0 14 14" fill="none" stroke="#f08434" stroke-width="1.2"><rect x="3.5" y="1" width="7" height="12" rx="1"/><line x1="6" y1="11" x2="8" y2="11"/></svg>
          +590 690 482 517
        </li>
        <li>
          <svg viewBox="0 0 14 14" fill="none" stroke="#f08434" stroke-width="1.2"><rect x="1" y="3" width="12" height="8"/><polyline points="1,3 7,8 13,3"/></svg>
          ceo@brightlanterncollective.com
        </li>
        <li>
          <svg viewBox="0 0 14 14" fill="none" stroke="#f08434" stroke-width="1.2"><circle cx="7" cy="7" r="5.8"/><ellipse cx="7" cy="7" rx="2.6" ry="5.8"/><line x1="1.2" y1="7" x2="12.8" y2="7"/></svg>
          www.brightlanterncollective.com
        </li>
      </ul>
      <div class="socials" aria-label="Social profiles">
        <span class="social-slot"></span>
        <span class="social-slot"></span>
        <span class="social-slot"></span>
      </div>
    </div>
  </section>
</main>
</body>
</html>
```